Business Cards, Stationery, Email signature
and Stationary
Business Cards, Stationery, Email signature - Construction
Creative Brief
Use specific fonts
looking for strong bold lettering
Bright & Fun-filled
Marta Quillen
President
2873 E Marlow Street Orange, CA 94153
marta@larkwoodltdroofing.com
larkwoodltdroofing.com
Was considering having a black business cards so I really wanted to logo to "pop". Even though we are construction I love a card that has personality and fun.

```html
<!DOCTYPE html>
<html lang="en">
<head>
<meta charset="utf-8">
<title>Larkwood Ltd – Business Card</title>
<link rel="stylesheet" href="https://fonts.googleapis.com/css2?family=Open+Sans:wght@400;700&display=swap">
<style>
  :root {
    --backdrop: #2b2b2b;
    --card-black: #050505;
    --olive-light: #a3ae8f;
    --olive-dark: #5f6d4e;
    --accent-orange: #f7931e;
    --brand-blue: #49a6dc;
    --ink-dark: #111111;
    --ink-light: #ffffff;
  }
  * { margin: 0; padding: 0; box-sizing: border-box; }
  html, body {
    width: 1200px; height: 787px; overflow: hidden;
    background: var(--backdrop);
    font-family: "Open Sans", Arial, sans-serif;
  }
  .canvas { position: relative; width: 1200px; height: 787px; }
  .card {
    position: absolute; left: 130px; top: 64px;
    width: 941px; height: 660px;
    border-radius: 34px; overflow: hidden;
    background: var(--card-black);
  }
  .card-shapes { position: absolute; inset: 0; }
  .holder { position: absolute; right: 70px; top: 120px; text-align: right; color: var(--ink-dark); }
  .holder-name { font-size: 37px; font-weight: 700; line-height: 1.1; }
  .holder-title { font-size: 20px; font-weight: 700; margin-top: 6px; }
  .brand { position: absolute; left: 86px; top: 252px; display: flex; align-items: center; gap: 26px; }
  .brand-dot { width: 104px; height: 104px; border-radius: 50%; background: var(--brand-blue); }
  .brand-name { font-size: 50px; font-weight: 400; color: var(--brand-blue); letter-spacing: 1px; }
  .address { position: absolute; left: 64px; top: 510px; color: var(--ink-light); font-size: 20px; font-weight: 700; line-height: 31px; }
  .contacts { position: absolute; left: 536px; top: 374px; list-style: none; color: var(--ink-light); font-size: 20px; font-weight: 700; }
  .contacts li { display: flex; align-items: center; height: 31.5px; }
  .contacts svg { width: 24px; height: 24px; margin-right: 20px; fill: none; stroke: var(--accent-orange); stroke-width: 2; stroke-linecap: round; stroke-linejoin: round; }
</style>
</head>
<body>
<div class="canvas">
  <div class="card">
    <svg class="card-shapes" viewBox="0 0 941 660" preserveAspectRatio="none" aria-hidden="true">
      <defs>
        <linearGradient id="olive" x1="0" y1="0" x2="1" y2="0.3">
          <stop offset="0" stop-color="var(--olive-light)"/>
          <stop offset="1" stop-color="var(--olive-dark)"/>
        </linearGradient>
      </defs>
      <rect width="941" height="660" fill="url(#olive)"/>
      <path d="M180,196 C480,186 760,290 941,412 L941,480 C760,340 480,212 180,204 Z" fill="var(--accent-orange)"/>
      <path d="M0,186 C60,186 130,200 180,204 C480,212 760,340 941,480 L941,660 L0,660 Z" fill="var(--card-black)"/>
    </svg>

    <div class="holder">
      <p class="holder-name">Marta Quillen</p>
      <p class="holder-title">President</p>
    </div>

    <div class="brand">
      <span class="brand-dot"></span>
      <span class="brand-name">Larkwood Ltd</span>
    </div>

    <p class="address">2873 E Marlow Street<br>Orange, CA 94153</p>

    <ul class="contacts">
      <li><svg viewBox="0 0 24 24"><path d="M5 3h4l2 5-3 2a12 12 0 0 0 6 6l2-3 5 2v4a2 2 0 0 1-2 2A17 17 0 0 1 3 5a2 2 0 0 1 2-2z"/></svg>888-204-5517</li>
      <li><svg viewBox="0 0 24 24"><path d="M3 9c0-3 18-3 18 0v2h-5V9H8v2H3z"/><path d="M6 13h12l2 7H4z"/><circle cx="12" cy="16.5" r="1.5"/></svg>714-390-2264</li>
      <li><svg viewBox="0 0 24 24"><rect x="7" y="2" width="10" height="20" rx="2"/><path d="M11 18h2"/></svg>714-813-4076</li>
      <li><svg viewBox="0 0 24 24"><path d="M7 9V3h10v6"/><rect x="3" y="9" width="18" height="8" rx="1"/><path d="M7 14h10v7H7z"/></svg>714-390-2265</li>
      <li><svg viewBox="0 0 24 24"><rect x="3" y="5" width="18" height="14" rx="1"/><path d="M3 6l9 7 9-7"/></svg>marta@larkwoodltdroofing.com</li>
      <li><svg viewBox="0 0 24 24"><circle cx="12" cy="12" r="9"/><path d="M3 12h18M12 3c3 3 3 15 0 18M12 3c-3 3-3 15 0 18"/></svg>larkwoodltdroofing.com</li>
    </ul>
  </div>
</div>
</body>
</html>
```